Designing a front label called Ice Secco / Bottle Label for a Sparkling Wine called Perla Neve

We want to bring a Perla Neve on the market. For this we need a front label. Bottle is painted white and the capsule is fixed. (Black with golden lettering K.Wendlicher) Height of label max. 8.5cm. The whole thing should be fresh teen. Happy with reference to Ice .... etc. Secco is the German version of Prosecco. But better. There are currently many Perla Neve on the market. We also want one now. www.wendlicher.de We have a nice white lacquered TRV bottle with capsule. it just fehtl the right label. Sender K.Wendlicher does not have to be on top ... but if it fits. Lettering is already in the capsule anyway.

Target Market(s)

Supermarket, gals, party, alcohol, RRP 4.99 €

Font styles to use
Decorative

Colors

Requirements
Must have
• Self-adhesive label, printable data in 4c, reference to ice, black, golden reference to the capsule.
Nice to have
• Ice cubes, cool, cool.
Should not have
• boredom

```html
<!DOCTYPE html>
<html lang="en">
<head>
<meta charset="utf-8">
<title>Perla Neve – Front Label</title>
<link rel="stylesheet" href="https://fonts.googleapis.com/css2?family=Berkshire+Swash&family=Pinyon+Script&family=Cinzel+Decorative:wght@700&display=swap">
<style>
  :root {
    --paper: #ffffff;
    --ink: #000000;
    --lemon: #f5ea8e;
    --frost: #ffffff;
  }
  html, body {
    margin: 0;
    padding: 0;
    width: 1200px;
    height: 852px;
    overflow: hidden;
    background: var(--paper);
  }
  .label-canvas {
    display: block;
    width: 1200px;
    height: 852px;
  }
  .frame-line { fill: none; stroke: var(--ink); stroke-width: 2; }
  .gold-border { fill: var(--lemon); }
  .label-field { fill: var(--ink); }
  .brand-word {
    font-family: "Berkshire Swash", "Georgia", serif;
    font-size: 90px;
    fill: var(--lemon);
  }
  .variety-word {
    font-family: "Pinyon Script", "Brush Script MT", cursive;
    font-size: 120px;
    fill: var(--frost);
    stroke: var(--lemon);
    stroke-width: 1.5;
  }
  .splash-area { fill: var(--lemon); }
  .tagline {
    font-family: "Cinzel Decorative", "Times New Roman", serif;
    font-weight: 700;
    font-size: 29px;
    fill: var(--ink);
  }
</style>
</head>
<body>
<svg class="label-canvas" viewBox="0 0 1200 852" xmlns="http://www.w3.org/2000/svg">
  <defs>
    <radialGradient id="iceGlow" cx="50%" cy="60%" r="55%">
      <stop offset="0%" stop-color="#9a9a9a" stop-opacity="0.55"/>
      <stop offset="100%" stop-color="#000000" stop-opacity="0"/>
    </radialGradient>
  </defs>

  <!-- outer double frame -->
  <rect class="frame-line" x="716" y="62" width="394" height="728"/>
  <rect class="frame-line" x="724" y="70" width="378" height="712"/>

  <!-- golden border and black field -->
  <rect class="gold-border" x="733" y="79" width="360" height="694"/>
  <rect class="label-field" x="740" y="86" width="346" height="680"/>

  <!-- ice imagery -->
  <rect x="770" y="100" width="290" height="310" fill="url(#iceGlow)" role="img" aria-label="Photograph of ice cubes splashing with rising bubbles"/>

  <!-- brand -->
  <text class="brand-word" x="913" y="466" text-anchor="middle">Perla</text>
  <rect x="835" y="476" width="160" height="20" fill="var(--lemon)" opacity="0.35" role="img" aria-label="Yellow scroll flourish"/>
  <text class="variety-word" x="913" y="606" text-anchor="middle">Neve</text>

  <!-- ornament and bottom splash area -->
  <rect x="898" y="628" width="30" height="34" fill="var(--lemon)" opacity="0.6" role="img" aria-label="Yellow fleur-de-lis ornament"/>
  <rect class="splash-area" x="740" y="668" width="346" height="98" role="img" aria-label="Yellow liquid splash illustration"/>
  <text class="tagline" x="913" y="746" text-anchor="middle">Lorem ipsum</text>
</svg>
</body>
</html>
```